Website design and coding for new consultancy company

I need to have a full website designed for a new consultancy business I'm trying to establish. It's called Brightpath consult. I need an English version to begin with, and then there should be a Danish version as well, but I'll translate that myself. Just be aware that I need two language versions. The consultancy field that I'm targeting is Leadership - and specialist development. I offer to facilitate corporate academies for global companies as well as specific workshops within leadership- or team development, strategy sessions, personal coaching and facilitation of D&I (Diversity and inclusion) workshops. BTW my logo is not in high resolution - I need that as well.

Target Market(s)

Larger companies that has a need for developing their inhouse leadership capabilities or that wants to develop their specialists to take on more responsibility.

Industry/Entity Type

Consultancy business

Coding

Number of Pages Required

5+ page

Requirements
Must have
• Introduction site with a catch phrase. Book a meeting. Services that's beeing offered. Blog site with white papers etc. Language toggle (Danish/English). Cases/testimonials. About site. Contact site.

```html
<!DOCTYPE html>
<html lang="en">
<head>
<meta charset="utf-8">
<title>Brightpath consult — Leadership &amp; Specialist Development</title>
<link href="https://fonts.googleapis.com/css2?family=Inter:wght@400;500;600;700;800&display=swap" rel="stylesheet">
<style>
:root{
  --navy:#0f1f3d;
  --ink:#1b2333;
  --muted:#5f6b7d;
  --line:#e3e7ee;
  --soft:#f4f6fa;
  --accent:#1f3f7a;
  --white:#ffffff;
}
*{box-sizing:border-box;margin:0;padding:0}
html,body{width:849px;height:1200px;overflow:hidden;background:var(--white)}
body{font-family:"Inter",Arial,sans-serif;color:var(--ink);position:relative;font-size:7px;line-height:1.4}
.wrap{position:absolute;left:120px;width:610px}
a{color:inherit;text-decoration:none}

.nav{position:absolute;top:0;left:0;width:849px;height:36px;border-bottom:1px solid var(--line)}
.brand{display:flex;align-items:center;gap:6px;font-weight:800;font-size:11px;color:var(--navy);letter-spacing:.5px}
.brand .mark{width:10px;height:10px;background:var(--navy)}
.nav .brand{position:absolute;left:120px;top:12px}
.nav-links{position:absolute;left:270px;top:11px;display:flex;gap:4px}
.nav-links a{padding:3px 7px;border-radius:3px;font-size:7px;color:var(--muted)}
.nav-links a.active{background:var(--soft);color:var(--navy);font-weight:600}
.lang{position:absolute;left:672px;top:11px;display:flex;gap:4px;font-size:7px}
.lang span{padding:3px 6px;border-radius:8px;color:var(--muted)}
.lang .on{background:var(--navy);color:var(--white);font-weight:600}

.hero{top:66px}
.hero h1{font-size:21px;line-height:1.2;font-weight:800;color:var(--navy);width:330px}
.hero p{margin-top:9px;width:300px;color:var(--muted);font-size:7.5px}
.btns{margin-top:14px;display:flex;gap:8px}
.btn{padding:6px 10px;border-radius:3px;font-size:7px;font-weight:600;border:1px solid var(--navy)}
.btn.primary{background:var(--navy);color:var(--white)}
.btn.ghost{color:var(--navy);background:var(--white)}
.why{position:absolute;left:460px;top:20px;width:150px;padding:10px 11px;border:1px solid var(--line);border-radius:5px;box-shadow:0 4px 12px rgba(15,31,61,.08);background:var(--white)}
.why h3{font-size:8px;color:var(--navy);margin-bottom:5px}
.why li{list-style:none;padding-left:7px;position:relative;color:var(--muted);font-size:6px;margin-bottom:3px}
.why li::before{content:"";position:absolute;left:0;top:3px;width:3px;height:3px;border-radius:50%;background:var(--accent)}

.partners{top:268px}
.partners p{color:var(--muted);font-size:6.5px;width:560px}
.logos{margin-top:14px;display:flex;gap:10px}
.logos span{padding:5px 10px;border:1px solid var(--line);border-radius:3px;font-size:6.5px;font-weight:600;color:var(--muted)}

h2{font-size:12px;font-weight:800;color:var(--navy)}
.sub{color:var(--muted);font-size:6.5px;margin-top:3px}
.services{top:380px}
.grid{margin-top:14px;display:grid;grid-template-columns:repeat(3,1fr);gap:10px}
.card{height:86px;border:1px solid var(--line);border-radius:5px;padding:10px}
.card h3{font-size:8px;color:var(--navy)}
.card p{color:var(--muted);font-size:6px;margin-top:3px;width:160px}
.card .btn{display:inline-block;margin-top:8px;padding:4px 7px;font-size:6px;font-weight:500;background:var(--white);color:var(--navy)}

.clients{top:672px}
.quotes{margin-top:14px;display:grid;grid-template-columns:1fr 1fr;gap:12px}
.quote{height:84px;border:1px solid var(--line);border-radius:5px;padding:10px 12px;box-shadow:0 2px 8px rgba(15,31,61,.05)}
.quote p{font-size:7px;color:var(--ink)}
.who{margin-top:10px;display:flex;align-items:center;gap:6px;color:var(--muted);font-size:6px}
.who i{width:12px;height:12px;border-radius:50%;background:var(--line);display:block}

.news{top:876px}
.news input{display:block;margin-top:10px;width:610px;height:18px;border:1px solid var(--line);border-radius:3px;padding:0 7px;font:6.5px "Inter",sans-serif;color:var(--muted)}
.news .btn{display:block;margin-top:8px;text-align:center}

.footer{position:absolute;top:996px;left:0;width:849px;border-top:1px solid var(--line);height:204px}
.footer .brand{position:absolute;left:120px;top:50px}
.tag{position:absolute;left:120px;top:70px;color:var(--muted);font-size:6.5px}
.col{position:absolute;top:46px;font-size:6.5px;color:var(--muted)}
.col h4{font-size:7px;color:var(--navy);margin-bottom:4px}
.col li{list-style:none;line-height:1.55}
.bottom{position:absolute;top:160px;left:120px;width:610px;border-top:1px solid var(--line);padding-top:8px;display:flex;justify-content:space-between;font-size:6px;color:var(--muted)}
</style>
</head>
<body>
<header class="nav">
  <div class="brand"><span class="mark"></span>BRIGHTPATH</div>
  <nav class="nav-links">
    <a class="active">Home</a><a>About</a><a>Services</a><a>Cases</a><a>Insights</a><a>Philosophy</a><a>FAQ</a><a>Contact</a>
  </nav>
  <div class="lang"><span class="on">EN</span><span>DA</span></div>
</header>

<section class="wrap hero">
  <h1>Transforming Leadership.<br>Empowering Specialists.<br>Elevating Performance.</h1>
  <p>We design corporate academies, specialist programs, and high-impact workshops that lift performance.</p>
  <div class="btns"><a class="btn primary">Book a free Consultation</a><a class="btn ghost">Download Whitepaper</a></div>
  <aside class="why">
    <h3>Why Brightpath?</h3>
    <ul>
      <li>Corporate academies for managers and future leaders</li>
      <li>Specialist programs that expand influence &amp; collaboration</li>
      <li>High-impact workshops and executive coaching</li>
    </ul>
  </aside>
</section>

<section class="wrap partners">
  <p>We partner with global companies to build leadership depth and empower specialists to influence across the business. Our programs are practical, measurable, and built around your context.</p>
  <div class="logos"><span>Norvik</span><span>Harbor Lane</span><span>Keldmark</span><span>Nordspan</span></div>
</section>

<section class="wrap services">
  <h2>What we do</h2>
  <p class="sub">Clarity, cadence and capability — delivered through programs and workshops.</p>
  <div class="grid">
    <div class="card"><h3>Corporate Academies</h3><p>Multi-level curricula for managers and future leaders at scale.</p><a class="btn">Explore Program</a></div>
    <div class="card"><h3>Specialist Development</h3><p>Enable experts to collaborate, influence and drive business outcomes.</p><a class="btn">Explore Program</a></div>
    <div class="card"><h3>Leadership Coaching</h3><p>1:1 executive or career coaching with measurable goals.</p><a class="btn">Explore Program</a></div>
    <div class="card"><h3>Team Development</h3><p>Align, build trust and deliver with shared ways of working.</p><a class="btn">Explore Program</a></div>
    <div class="card"><h3>Workshops &amp; Facilitation</h3><p>D&amp;I, conflict, feedback and strategy sessions tailored to your context.</p><a class="btn">Explore Program</a></div>
  </div>
</section>

<section class="wrap clients">
  <h2>What clients say</h2>
  <div class="quotes">
    <div class="quote"><p>“Brightpath enabled rapid alignment and execution across our leadership group. We saw 40% improvement in cross-functional collaboration within 6 months.”</p><div class="who"><i></i>Director, Global L&amp;D</div></div>
    <div class="quote"><p>“Practical tools, clear language and strong facilitation — immediate impact. Our manager NPS scores increased from 6.2 to 8.7 in just 3 months.”</p><div class="who"><i></i>SVP, Operations</div></div>
  </div>
</section>

<section class="wrap news">
  <h2>Never miss an insight</h2>
  <p class="sub">Get leadership articles and frameworks straight to your inbox.</p>
  <input type="email" placeholder="you@company.com">
  <a class="btn primary">Subscribe</a>
</section>

<footer class="footer">
  <div class="brand"><span class="mark"></span>BRIGHTPATH</div>
  <p class="tag">Improving Performance</p>
  <div class="col" style="left:420px"><h4>Quick links</h4><ul><li>Home</li><li>About</li><li>Services</li><li>Cases</li><li>Insights</li><li>FAQ</li><li>Contact</li></ul></div>
  <div class="col" style="left:580px"><h4>Contact</h4><ul><li>CVR: 41027735</li><li>Lindholm Allé 14, 2300</li><li>Copenhagen S</li><li>hello@brightpath.consult</li><li>LinkedIn</li></ul></div>
  <div class="bottom"><span>© 2025 Brightpath consult</span><span>Privacy Policy · Cookie Policy</span></div>
</footer>
</body>
</html>
```